Business Card Design

I'm a commercial general contractor remodel offices, hotels, health clubs and stores mostly San Francisco and the peninsula
the file I down loaded is kind of what I want I like the I beam with my company name in it, that would be fine with me but if you have better Idea will look at it you never know, I'm decided to give in and change my company name to how every one knows me, I have been in business since 1991, I like the I beam logo I included one of my old card from my old company for reference for you.

Industry/Entity Type

Business

Contact Information for Business Card

BRAXO CONSTRUCTION (is my company name)
Wendell Trusk contractor, LIc 314827
4158 Garnet Row, San Bruno, California 94066
mobile, (415) 555-0147
phone (650) 555-0182
Fax, (650) 555-0183
email, braxo@braxoconstruction.example

```html
<!DOCTYPE html>
<html lang="en">
<head>
<meta charset="utf-8">
<title>Braxo Construction – Business Cards</title>
<link rel="stylesheet" href="https://fonts.googleapis.com/css2?family=Open+Sans:wght@400;600;700&family=Tinos&display=swap">
<style>
  :root {
    --page-bg: #e4e1da;
    --cream: #f1efe7;
    --ink: #1c2733;
    --navy: #0f2237;
    --navy-accent: #3a7fc2;
    --blue: #2b86cf;
    --blue-accent: #10263e;
    --white: #ffffff;
    --mark: #e6ebf1;
  }
  * { box-sizing: border-box; margin: 0; padding: 0; }
  html, body { width: 1200px; height: 900px; overflow: hidden; }
  body {
    background: var(--page-bg);
    font-family: "Open Sans", Arial, sans-serif;
    display: flex;
    align-items: center;
    justify-content: center;
    gap: 120px;
  }
  .card {
    width: 340px;
    height: 595px;
    background: var(--cream);
    display: flex;
    flex-direction: column;
    box-shadow: 0 2px 6px rgba(0,0,0,0.15);
  }
  .card-header {
    height: 86px;
    display: flex;
    flex-direction: column;
    align-items: center;
    justify-content: center;
    color: var(--ink);
    font-weight: 700;
    line-height: 1.05;
  }
  .company-name { font-size: 31px; letter-spacing: 1px; }
  .company-type { font-size: 21px; font-weight: 600; }
  .card-body {
    height: 342px;
    display: flex;
    flex-direction: column;
    align-items: center;
    color: var(--white);
    text-align: center;
  }
  .card--navy .card-body { background: var(--navy); }
  .card--blue .card-body { background: var(--blue); }
  .brand-name {
    margin-top: 46px;
    height: 40px;
    display: flex;
    align-items: center;
    color: var(--mark);
    font-weight: 700;
    font-size: 30px;
    letter-spacing: 1px;
  }
  .person-name {
    margin-top: 36px;
    font-family: "Tinos", "Times New Roman", serif;
    font-size: 21px;
    text-transform: uppercase;
    letter-spacing: 0.5px;
  }
  .card--navy .person-name, .card--navy .person-role { color: var(--navy-accent); }
  .card--blue .person-name, .card--blue .person-role { color: var(--blue-accent); }
  .person-role {
    font-family: "Tinos", "Times New Roman", serif;
    font-size: 14px;
    margin-top: 1px;
  }
  .licence { margin-top: 30px; font-size: 19px; }
  .phone-line { font-size: 13px; margin-top: 5px; }
  .card-footer {
    flex: 1;
    display: flex;
    flex-direction: column;
    align-items: center;
    justify-content: center;
    gap: 4px;
    color: var(--ink);
    font-size: 12.5px;
    text-align: center;
  }
</style>
</head>
<body>
  <article class="card card--navy">
    <header class="card-header">
      <span class="company-name">BRAXO</span>
      <span class="company-type">CONSTRUCTION</span>
    </header>
    <section class="card-body">
      <p class="brand-name">Braxo</p>
      <p class="person-name">Wendell Trusk</p>
      <p class="person-role">Constructor</p>
      <p class="licence">Lic #314827</p>
      <p class="phone-line">Telephone : (650)555-0182</p>
      <p class="phone-line">Cell : (415)555-0147</p>
    </section>
    <footer class="card-footer">
      <p>Fax : (650) 555-0183</p>
      <p>Email : braxo@braxoconstruction.example</p>
      <p>www.braxoconstruction.example</p>
      <p>Add : 4158 Garnet Row San Bruno, Ca 94066</p>
    </footer>
  </article>

  <article class="card card--blue">
    <header class="card-header">
      <span class="company-name">BRAXO</span>
      <span class="company-type">CONSTRUCTION</span>
    </header>
    <section class="card-body">
      <p class="brand-name">Braxo</p>
      <p class="person-name">Wendell Trusk</p>
      <p class="person-role">Constructor</p>
      <p class="licence">Lic #314827</p>
      <p class="phone-line">Telephone : (650)555-0182</p>
      <p class="phone-line">Cell : (415)555-0147</p>
    </section>
    <footer class="card-footer">
      <p>Fax : (650) 555-0183</p>
      <p>Email : braxo@braxoconstruction.example</p>
      <p>www.braxoconstruction.example</p>
      <p>Add : 4158 Garnet Row San Bruno, Ca 94066</p>
    </footer>
  </article>
</body>
</html>
```